New Business Card Design Project

Use the flyer uploaded and website www.brightoakbuilders.com for inspiration.
List Our Services on Backside of business cards
Martin Hollis
Harborline Renovations Inc.
Licensed General Contractors
858-471-9063

Contact Information for Business Card

Use the flyer uploaded and website www.brightoakbuilders.com for inspiration. List Our Services on Backside of business cards Martin Hollis Harborline Renovations Inc. Licensed General Contractors 858-471-9063

```html
<!DOCTYPE html>
<html lang="en">
<head>
<meta charset="utf-8">
<title>Harborline Renovations – Business Card</title>
<link href="https://fonts.googleapis.com/css2?family=Cinzel:wght@400&family=Jost:wght@400;500&display=swap" rel="stylesheet">
<style>
  :root {
    --backdrop: #d9d9d9;
    --card-dark: #22242b;
    --card-light: #ececea;
    --copper: #c98a69;
    --ink: #1a1a1a;
    --ink-soft: #2b2b2b;
  }
  * { margin: 0; padding: 0; box-sizing: border-box; }
  html, body {
    width: 1200px;
    height: 879px;
    overflow: hidden;
    background: var(--backdrop);
  }
  .canvas {
    position: relative;
    width: 1200px;
    height: 879px;
  }
  .card {
    position: absolute;
    width: 540px;
    height: 309px;
    border-radius: 3px;
    box-shadow: 0 10px 30px rgba(0,0,0,0.18);
  }
  .card--front {
    left: 70px;
    top: 150px;
    background: var(--card-dark);
    display: flex;
    align-items: center;
    justify-content: center;
  }
  .brand {
    display: flex;
    align-items: center;
    gap: 16px;
  }
  .brand__mark {
    width: 14px;
    height: 14px;
    border-radius: 50%;
    background: var(--copper);
  }
  .brand__name {
    font-family: "Cinzel", serif;
    font-weight: 400;
    font-size: 27px;
    letter-spacing: 1px;
    color: var(--copper);
  }
  .card--back {
    left: 590px;
    top: 420px;
    background: var(--card-light);
    padding: 0 0 46px 44px;
    display: flex;
    flex-direction: column;
    justify-content: flex-end;
  }
  .contact__person {
    font-family: "Jost", sans-serif;
    font-weight: 500;
    font-size: 19px;
    letter-spacing: 1px;
    color: var(--ink);
    margin-bottom: 8px;
  }
  .contact__company {
    font-family: "Cinzel", serif;
    font-size: 24px;
    color: var(--ink-soft);
    line-height: 1.1;
    margin-bottom: 6px;
  }
  .contact__licence {
    font-family: "Jost", sans-serif;
    font-size: 18px;
    letter-spacing: 1.4px;
    color: var(--ink);
    margin-bottom: 6px;
  }
  .contact__phone {
    display: flex;
    align-items: center;
    gap: 10px;
    font-family: "Jost", sans-serif;
    font-weight: 500;
    font-size: 24px;
    letter-spacing: 1.5px;
    color: var(--ink);
  }
  .contact__phone svg { width: 20px; height: 20px; }
</style>
</head>
<body>
<main class="canvas">
  <section class="card card--front" aria-label="Card front">
    <div class="brand">
      <span class="brand__mark"></span>
      <span class="brand__name">Harborline Renovations</span>
    </div>
  </section>

  <section class="card card--back" aria-label="Card back">
    <p class="contact__person">Martin Hollis</p>
    <p class="contact__company">HARBORLINE RENOVATIONS INC.</p>
    <p class="contact__licence">Licensed General Contractors</p>
    <p class="contact__phone">
      <svg viewBox="0 0 20 20" aria-hidden="true">
        <circle cx="10" cy="10" r="9" fill="none" stroke="#1a1a1a" stroke-width="1.2"/>
        <path d="M7 5.5c.4-.3.9-.2 1.1.2l.8 1.6c.2.4.1.8-.2 1.1l-.6.5c.5 1.1 1.3 1.9 2.3 2.4l.5-.6c.3-.3.7-.4 1.1-.2l1.6.8c.4.2.5.7.2 1.1l-.6.8c-.4.5-1.1.7-1.7.5C9.2 12.7 7.3 10.8 6.4 8.5c-.2-.6 0-1.3.5-1.7z" fill="#1a1a1a"/>
      </svg>
      858-471-9063
    </p>
  </section>
</main>
</body>
</html>
```